New Website for ReBranded Company - CrewBeacon

We have a successful company and website currently but it is a little dated. We have re-branded the company from Harbor Signal Networks to CrewBeacon and have a new logo for the new name. We are looking to build a newer fresher website with the new name. I will need a concept of the home page and one inside page. You can see our current site at https://www.harborsignalnetworks.example and the new site will be https://www.crewbeacon.example .

I also really like the https://www.pathlantern.example/ website. I like ledgerkite.example website. I like the https://skillorbit.example/ website.

See the attached document for layout and some text to use. Use the pictures I attached as opposed to pictures from the old site as much as you can.

Target Market(s)

Business

Industry/Entity Type

Software Service

Number of Pages Required

2 page

Font styles to use
Sans Serif

Requirements
Must have
• Use the colors from my logo. Professional but modern. We want people to feel like our product makes their staff feel safer at work.
Should not have
• Don't use any red or orange (no stop colors).

```html
<!DOCTYPE html>
<html lang="en">
<head>
<meta charset="utf-8">
<title>CrewBeacon – Your Staff is Protected</title>
<link href="https://fonts.googleapis.com/css2?family=Ubuntu:wght@500;700&family=Open+Sans:wght@400;600;700&family=Roboto:wght@400;500;700&display=swap" rel="stylesheet">
<style>
:root{
  --green:#8cc652;
  --green-light:#9dd066;
  --green-btn:#72b640;
  --green-text:#5aa82a;
  --green-rule:#8cc652;
  --green-deep:#3f8a22;
  --teal:#2f9e8f;
  --blue:#4a90e2;
  --ink:#333a33;
  --ink-soft:#555;
  --white:#fff;
  --cream:#fbf6dc;
}
*{box-sizing:border-box;margin:0;padding:0}
html,body{width:1200px;height:3564px;overflow:hidden}
body{position:relative;background:var(--white);font-family:"Open Sans",sans-serif;color:var(--ink)}
.abs{position:absolute}
.heading{font-family:"Ubuntu",sans-serif;font-weight:700}
.btn{position:absolute;display:flex;align-items:center;justify-content:center;font-family:"Roboto",sans-serif;font-weight:700;font-size:17px;text-decoration:none}
.btn-solid{background:var(--green-btn);color:var(--white)}
.btn-white{background:var(--white);color:var(--green-btn)}
.brand{display:flex;align-items:center;gap:10px;font-family:"Ubuntu",sans-serif;font-weight:500;font-size:25px}
.brand-dot{width:30px;height:30px;border-radius:50%}

/* hero */
.hero{left:0;top:0;width:1200px;height:519px;background:linear-gradient(90deg,#8ac24d,#9ed26a)}
.nav{left:502px;top:22px;display:flex;gap:20px;font-family:"Roboto",sans-serif;font-size:16px;color:var(--white)}
.nav-outline{left:786px;top:14px;width:128px;height:41px;border:2px solid var(--white);color:var(--white);font-weight:500;font-size:17px}
.nav-solid{left:920px;top:14px;width:129px;height:41px;background:var(--green-btn);color:var(--white);font-weight:500;font-size:17px}
.hero-title{left:149px;top:138px;font-size:40px;line-height:52px;color:var(--white);letter-spacing:.5px}
.hero-copy{left:149px;top:260px;width:420px;font-size:14px;line-height:20px;color:var(--white)}
.hero-strong{left:149px;top:314px;font-family:"Roboto",sans-serif;font-weight:700;font-size:16.5px;color:var(--white)}
.hero-cta{left:149px;top:382px;width:229px;height:55px}
.hero-photo{left:630px;top:118px;width:491px;height:332px;border:7px solid #f4f4f4;background:linear-gradient(135deg,#e9e9e9,#d4d6d6 60%,#c9cdd1);box-shadow:0 2px 8px rgba(0,0,0,.15)}

/* features */
.feature{top:547px;width:208px}
.feature svg{display:block;height:92px}
.feature-rule{height:2px;background:var(--green-rule);margin-top:8px}
.feature p{margin-top:18px;font-size:14px;line-height:20px;color:var(--ink-soft)}

/* alone section */
.alone-title{left:149px;top:847px;font-family:"Ubuntu",sans-serif;font-weight:500;font-size:32px;line-height:45px;color:var(--ink)}
.alone-q{left:150px;top:964px;width:430px;font-size:19px;line-height:27px;color:var(--ink)}
.alone-q p+p{margin-top:12px}
.alone-copy{left:150px;top:1083px;width:430px;font-size:13.5px;line-height:20.5px;color:var(--ink)}
.alone-cta{left:149px;top:1201px;width:212px;height:51px}
.desk-photo{left:765px;top:786px;width:435px;height:536px;background:linear-gradient(160deg,#5d5f60,#8c8e8c 40%,#b8bbb6 70%,#7e817e)}
.phone{left:648px;top:851px;width:206px;height:422px;background:#f1f1f1;border-radius:30px;border:2px solid #d8d8d8;box-shadow:0 4px 14px rgba(0,0,0,.2)}
.phone-screen{position:absolute;left:12px;top:14px;right:12px;bottom:14px;background:var(--white);border-radius:18px;overflow:hidden;font-family:"Roboto",sans-serif}
.ph-bar{height:40px;padding:10px 8px 0;font-size:8px;color:#444}
.ph-search{margin:4px 6px;height:14px;border:1px solid #ddd;font-size:6px;color:#aaa;padding:2px 4px}
.ph-row{display:flex;align-items:center;gap:6px;margin:6px 6px;height:28px;border-left:3px solid;padding-left:6px;font-size:6.5px;font-weight:700;color:#333;box-shadow:0 1px 3px rgba(0,0,0,.12)}
.ph-row .tag{margin-left:auto;margin-right:6px;font-size:5px;color:#fff;padding:3px 6px;border-radius:2px}
.ph-big{position:absolute;left:6px;right:6px;height:26px;display:flex;align-items:center;padding:0 8px;font-size:7px;font-weight:700;color:#fff;border-radius:2px}
.ph-big .tag{margin-left:auto;background:#fff;color:#999;font-size:5px;padding:3px 6px}

/* why */
.why{left:0;top:1396px;width:1200px;height:475px;background:var(--green)}
.why-title{left:0;top:1404px;width:1200px;text-align:center;font-size:48px;color:var(--white);letter-spacing:.5px}
.why-col{top:1530px;color:var(--white)}
.why-col h3{font-family:"Roboto",sans-serif;font-weight:700;font-size:19px;line-height:26px;margin-top:12px}
.why-col p,.why-col li{font-size:14px;line-height:20px}
.why-list{display:grid;grid-template-columns:118px 120px;list-style:none;margin-top:4px}
.why-list li::before{content:"•";margin-right:7px}
.why-cta{left:490px;top:1789px;width:217px;height:51px}
.arc{top:1514px}

/* scary */
.man-photo{left:0;top:1949px;width:378px;height:534px;background:linear-gradient(180deg,#2b3540,#1f2730 60%,#c9bfb2 92%)}
.dash{left:118px;top:2039px;width:517px;height:351px;background:var(--white);border:4px solid #eee;box-shadow:0 3px 12px rgba(0,0,0,.25);font-family:"Roboto",sans-serif;overflow:hidden}
.dash-top{height:34px;border-bottom:1px solid #e3e3e3;display:flex;align-items:center;padding:0 12px;font-size:11px;letter-spacing:1px;color:#333;gap:10px}
.dash-top .user{margin-left:auto;font-size:7px;letter-spacing:0;border:1px solid #ddd;padding:3px 8px}
.dash-left{position:absolute;left:0;top:34px;width:180px;bottom:0;border-right:1px solid #eee;font-size:7px;color:#333}
.dash-chat{position:absolute;left:192px;top:42px;right:36px;font-size:7px;color:#555}
.bubble{background:var(--cream);padding:8px 10px;margin-top:10px;height:56px;font-style:italic;color:#888}
.bubble span{display:block;font-style:normal;color:#555;margin-top:12px}
.scary-title{left:657px;top:2052px;font-family:"Ubuntu",sans-serif;font-weight:500;font-size:33px;line-height:45px;color:var(--ink);letter-spacing:.3px}
.scary-copy{left:657px;top:2220px;width:420px;font-size:19px;line-height:28px;color:var(--ink)}
.stat{font-family:"Ubuntu",sans-serif;font-weight:700;font-size:48px;color:var(--green-text);letter-spacing:1px}
.stat-small{font-size:22px;font-family:"Ubuntu",sans-serif;font-weight:500;color:var(--ink)}
.stats{left:657px;top:2268px;line-height:52px}

/* plan */
.plan-title{left:0;top:2556px;width:1200px;text-align:center;font-size:48px;color:var(--ink)}
.step-num{top:2653px;width:36px;height:36px;border:2px solid var(--green-btn);border-radius:50%;display:flex;align-items:center;justify-content:center;font-family:"Roboto",sans-serif;font-size:17px;color:var(--ink)}
.card{top:2714px;width:265px;height:286px;background:var(--green);color:var(--white);padding:38px 18px 38px 27px}
.card h3{font-family:"Ubuntu",sans-serif;font-weight:500;font-size:23px;line-height:31px;white-space:nowrap}
.card ul{list-style:none;margin-top:10px;font-size:16px;line-height:22px}
.card li::before{content:"• "}
.card p{margin-top:14px;font-size:15.5px;line-height:22px}
.card-raised{box-shadow:0 4px 14px rgba(0,0,0,.3)}
.connector{top:2868px;height:0;border-top:2px dashed var(--green);width:54px}
.plan-cta{left:490px;top:3046px;width:217px;height:50px}

/* cta band */
.band{left:0;top:3155px;width:1200px;height:142px;background:var(--green)}
.band-text{left:152px;top:3212px;font-family:"Roboto",sans-serif;font-size:23px;color:var(--white)}
.band-btn{left:747px;top:3204px;width:249px;height:57px;font-weight:400;font-size:23px}

/* footer */
.footer .brand{left:149px;top:3342px;color:var(--green-text);font-size:29px}
.footer .brand-dot{background:var(--green-text);width:34px;height:34px}
.foot-rule{left:149px;top:3402px;width:322px;height:2px;background:var(--green-rule)}
.socials{left:149px;top:3415px;display:flex;gap:6px}
.socials span{width:56px;height:56px;border-radius:50%;background:var(--green-btn)}
.foot-col{font-family:"Roboto",sans-serif;color:var(--ink)}
.foot-col h4{font-family:"Ubuntu",sans-serif;font-weight:500;font-size:22px;margin-bottom:10px}
.foot-col ul{list-style:none;font-size:13.5px;line-height:20.5px}
.foot-col li{padding-left:15px;position:relative}
.foot-col li::before{content:"";position:absolute;left:0;top:8px;width:5px;height:5px;border-radius:50%;background:var(--green-btn)}
.foot-line{left:149px;top:3504px;width:900px;height:1px;background:#999}
.copyright{left:153px;top:3513px;font-size:13px}
.disclaimer{left:329px;top:3510px;width:510px;font-size:9.5px;line-height:13px}
.callus{left:862px;top:3513px;font-size:13px;font-family:"Roboto",sans-serif}
</style>
</head>
<body>

<!-- HERO -->
<section class="abs hero"></section>
<div class="abs brand" style="left:149px;top:16px;color:#fff"><span class="brand-dot" style="background:#fff"></span>CrewBeacon</div>
<nav class="abs nav"><span>Home</span><span>Buy Addons</span><span>Cust Login</span></nav>
<a class="btn nav-outline">Sign Up</a>
<a class="btn nav-solid">Sign Up</a>
<h1 class="abs heading hero-title">Feel Confident,<br>Your Staff is Protected</h1>
<p class="abs hero-copy">Lorem ipsum dolor sit amet, consectetur adipisicing elit, sed do eiusmod tempor incididunt ut labore et dolore</p>
<p class="abs hero-strong">Get a revolutionary new electronic panic button</p>
<a class="btn btn-white hero-cta">Sign Up</a>
<div class="abs hero-photo" role="img" aria-label="Photo of a young employee using the alert app on a phone, with a Get Assistance bubble"></div>

<!-- FEATURES -->
<div class="abs feature" style="left:149px">
  <svg viewBox="0 0 80 92" width="80"><g fill="#7cbf3f"><rect x="20" y="8" width="11" height="46" rx="5.5"/><rect x="33" y="2" width="11" height="50" rx="5.5"/><rect x="46" y="6" width="11" height="48" rx="5.5"/><rect x="59" y="14" width="10" height="42" rx="5"/><path d="M6 44c5-4 10 0 14 6V70c0 10 8 18 18 18h8c13 0 23-10 23-23V48H20L8 40z"/></g></svg>
  <div class="feature-rule"></div>
  <p>Problems Stopped Before They Start For Any Type Of Organization</p>
</div>
<div class="abs feature" style="left:491px">
  <svg viewBox="0 0 92 92" width="92"><circle cx="46" cy="46" r="44" fill="#7cbf3f"/><text x="46" y="64" text-anchor="middle" font-family="Open Sans,sans-serif" font-size="52" fill="#fff">$</text></svg>
  <div class="feature-rule"></div>
  <p>Affordable Prices Starting at $18per month. No Contracts. No Hidden Costs.</p>
</div>
<div class="abs feature" style="left:837px">
  <svg viewBox="0 0 90 92" width="90"><rect x="2" y="4" width="76" height="52" rx="3" fill="#7cbf3f"/><rect x="8" y="10" width="64" height="38" fill="#fff"/><rect x="30" y="56" width="20" height="10" fill="#7cbf3f"/><rect x="20" y="66" width="40" height="5" fill="#7cbf3f"/><rect x="56" y="36" width="30" height="52" rx="4" fill="#7cbf3f" stroke="#fff" stroke-width="3"/><rect x="61" y="43" width="20" height="34" fill="#fff"/></svg>
  <div class="feature-rule"></div>
  <p>Alerts by computer, mobile device, text,phone, email, monitoring and E911</p>
</div>

<!-- ALONE -->
<h2 class="abs alone-title">Your Employees Shouldn’t Feel<br>Alone When They Need Help</h2>
<div class="abs alone-q"><p>Does this problem make you feel frustrated and anxious?</p><p>Put a simple solution in their hands</p></div>
<p class="abs alone-copy">Lorem ipsum dolor sit amet, consectetur adipisicing elit, sed do eiusmod tempor incididunt ut labore et dolore magna aliqua. Ut enim ad minim veniam, quis nostrud exercitation ullamco laboris nisi ut aliquip ex ea commodo consequat. Duis</p>
<a class="btn btn-solid alone-cta">Get Started</a>
<div class="abs desk-photo" role="img" aria-label="Photo of a hand pressing a panic button mounted under a desk"></div>
<div class="abs phone">
  <div class="phone-screen">
    <div class="ph-bar">9:22<br><span style="display:inline-block;width:9px;height:9px;border-radius:50%;background:var(--green-deep);vertical-align:middle;margin-right:4px"></span>NORTHWIND SUPPLY<div style="font-size:4.5px;color:#999;text-align:center">WE ARE HERE FOR YOU</div></div>
    <div class="ph-search">Search alerts</div>
    <div class="ph-row" style="border-color:var(--green)">⚠ INTERNET DOWN. I<br>CAN'T WORK<span class="tag" style="background:var(--green-btn)">Raise alert</span></div>
    <div class="ph-row" style="border-color:var(--blue)">⚠ MAINTENANCE<br>REQUEST<span class="tag" style="background:var(--blue)">Raise alert</span></div>
    <div class="ph-big" style="top:322px;background:var(--teal)">⚠ I NEED ASSISTANCE<span class="tag">Raise alert</span></div>
    <div class="ph-big" style="top:355px;background:var(--green-deep)">⚠ EMERGENCY<span class="tag">Raise alert</span></div>
  </div>
</div>

<!-- WHY -->
<section class="abs why"></section>
<h2 class="abs heading why-title">Why Businesses choose us</h2>
<svg class="abs arc" style="left:282px" width="175" height="50"><path d="M2 46C50 -8 125 -8 173 46" fill="none" stroke="#fff" stroke-dasharray="3 4" stroke-width="1.5" opacity=".8"/></svg>
<svg class="abs arc" style="left:634px" width="175" height="50"><path d="M2 46C50 -8 125 -8 173 46" fill="none" stroke="#fff" stroke-dasharray="3 4" stroke-width="1.5" opacity=".8"/></svg>
<div class="abs why-col" style="left:151px;width:225px">
  <svg width="56" height="60" viewBox="0 0 56 60"><g fill="#dff2c4"><rect x="6" y="26" width="10" height="30" rx="5" transform="rotate(-35 11 41)"/><path d="M20 22l28 22-10 14-24-16z"/><rect x="40" y="8" width="10" height="26" rx="5" transform="rotate(35 45 21)"/></g><path d="M14 4l4 8M24 0v9M32 4l-4 8" stroke="#dff2c4" stroke-width="3"/></svg>
  <h3>EASY TO USE</h3>
  <p style="margin-top:52px">Press a button and let the right peopleknow you need help and open a chatwindow letting everyone talk on resolving their problem.</p>
</div>
<div class="abs why-col" style="left:440px;width:260px">
  <svg width="70" height="60" viewBox="0 0 70 60"><g fill="#dff2c4"><circle cx="16" cy="10" r="8"/><rect x="4" y="20" width="24" height="16" rx="4"/><rect x="34" y="2" width="18" height="14" rx="2"/><circle cx="54" cy="14" r="8"/><rect x="2" y="40" width="66" height="18" rx="2"/></g></svg>
  <h3>COMMUNICATE THE WAY<br>YOU WANT</h3>
  <p style="margin-top:14px;margin-left:4px">We give you lots of options:</p>
  <ul class="why-list" style="margin-left:4px"><li>Computer</li><li>Text</li><li>Mobile</li><li>E911</li><li>Email</li><li>Call Center</li><li>Phone call</li></ul>
</div>
<div class="abs why-col" style="left:767px;width:290px">
  <svg width="60" height="60" viewBox="0 0 60 60" style="margin-left:112px"><circle cx="30" cy="30" r="29" fill="#dff2c4"/><text x="30" y="42" text-anchor="middle" font-family="Open Sans,sans-serif" font-size="34" fill="#8cc652">$</text></svg>
  <h3>COST EFFECTIVE PROTECTION</h3>
  <p style="margin-top:52px;width:230px">By leveraging your existing network and equipment we can lower your costs to give better options to your staff.</p>
</div>
<a class="btn btn-white why-cta">Get Started</a>

<!-- SCARY -->
<div class="abs man-photo" role="img" aria-label="Photo of a staff member wearing a lanyard with a wearable alert button"></div>
<div class="abs dash">
  <div class="dash-top"><span style="width:26px;height:14px;border-radius:50%;background:var(--green-deep)"></span>NORTHWIND SUPPLY<span class="user">👤 Sam Porter ▾</span></div>
  <div class="dash-left">
    <div style="padding:6px 8px">&lt;&lt; Go back to the list</div>
    <svg width="30" height="28" style="position:absolute;left:67px;top:40px"><path d="M15 2L29 26H1z" fill="#111"/><rect x="13.5" y="9" width="3" height="10" fill="#fff"/><rect x="13.5" y="21" width="3" height="3" fill="#fff"/></svg>
    <div style="position:absolute;left:0;width:180px;top:76px;text-align:center;font-size:12px">Emergency</div>
    <div style="position:absolute;left:56px;top:104px;border:1px solid var(--blue);color:var(--blue);padding:3px 10px">End alert</div>
    <div style="position:absolute;left:8px;top:165px;line-height:26px">Alert<br>details:</div>
    <div style="position:absolute;left:70px;top:168px;line-height:26px">▣ 8/8/2020<br>◷ 9:26 AM<br>👤 Sam Porter<br>⌖ 120 Maple Court, Fairview</div>
  </div>
  <div class="dash-chat">
    <div>Alert chat:</div>
    <div class="bubble">Text notifications were sent to: Dana Reyes.<span>◁ Beacon Notify 9:26 AM</span></div>
    <div class="bubble">Voice call notifications were sent to: 0 users.<span>◁ Beacon Notify 9:26 AM</span></div>
    <div class="bubble">Push notifications were sent to: 0 users.<span>◁ Beacon Notify 9:26 AM</span></div>
    <div style="background:#e8edf2;width:190px;margin:10px 0 0 30px;padding:8px 10px;height:54px">I am on my way<span style="display:block;margin-top:12px">👤 Dana Reyes 9:28 AM</span></div>
  </div>
</div>
<h2 class="abs scary-title">We know how scary it<br>can feel to worry about<br>employee safety.</h2>
<p class="abs scary-copy">That’s why we have provided a way for customers to get help to staff effectively in</p>
<div class="abs stats"><span class="stat">45 States</span> <span class="stat-small">covering</span><br><span class="stat">5 counteries</span></div>

<!-- PLAN -->
<h2 class="abs heading plan-title">Simple Start Plan</h2>
<div class="abs step-num" style="left:263px">1</div>
<div class="abs step-num" style="left:580px">2</div>
<div class="abs step-num" style="left:900px">3</div>
<div class="abs connector" style="left:412px"></div>
<div class="abs connector" style="left:731px"></div>
<div class="abs card" style="left:148px;padding-left:31px"><h3>Explore Your<br>Choices</h3><ul><li>Pricing</li><li>Trial</li><li>Quote</li><li>Hardware</li></ul></div>
<div class="abs card card-raised" style="left:466px"><h3 style="margin-top:4px">Get Setup</h3><ul style="margin-top:20px"><li>Input Your Alerts</li><li>Input Your Staff</li><li>Install Our Software</li></ul></div>
<div class="abs card" style="left:785px"><h3>Feel Confident Your<br>Staff Is Protected</h3><p>High Five. You just took a major step to get rid of the anxiety and frustration this gave you</p></div>
<a class="btn btn-solid plan-cta">Get Started</a>

<!-- CTA BAND -->
<section class="abs band"></section>
<p class="abs band-text">Stay Connected with Staff during a Crisis Situations</p>
<a class="btn btn-white band-btn">Take free trial</a>

<!-- FOOTER -->
<footer class="footer">
  <div class="abs brand"><span class="brand-dot"></span>CrewBeacon</div>
  <div class="abs foot-rule"></div>
  <div class="abs socials" aria-label="Social links"><span></span><span></span><span></span><span></span><span></span></div>
  <div class="abs foot-col" style="left:540px;top:3333px"><h4 style="margin-left:14px">Shop</h4><ul><li>Add Ons</li><li>Start My Demo</li><li>Custom Quote</li><li>Start Trial</li></ul></div>
  <div class="abs foot-col" style="left:693px;top:3333px"><h4 style="margin-left:14px">About</h4><ul style="width:110px"><li>Affiliates</li><li>Contact</li><li>Support</li><li>Existing Customers</li></ul></div>
  <div class="abs foot-col" style="left:800px;top:3368px"><ul><li>Industries</li><li>Blog</li><li>FAQ</li></ul></div>
  <div class="abs foot-col" style="left:921px;top:3333px"><h4 style="margin-left:23px">Legal</h4><ul style="width:140px"><li>Privacy Policy</li><li>Terms of Use</li><li>End User License Agreement</li></ul></div>
  <div class="abs foot-line"></div>
  <p class="abs copyright">©CrewBeacon 2020</p>
  <p class="abs disclaimer">When employees feel alone during a threatening situation, we give them a way to let the right resources know that they need help so you can feel confident that your staff is protected.</p>
  <p class="abs callus">Call Us : 1 – 800 – 555 - 0142</p>
</footer>

</body>
</html>
```